QTR tub packaging design

Hi!
We require a design for two different flavours of packaging for a protein recovery formula.
The design will be for the cardboard tubs as in pic attached. The name of the product will be 'LW recovery formula'. The LW logo is also attached and can be slightly adjusted.
The project will require a design for the front and then a basic design for the information on the back. This will include ingredients, nutrition info, directions and production location. On the back it will also need the 'lift your stride' logo and something referring to 'LW recovery formula by 'Your Vital Ember' (logo for this is attached).
The product will come in two flavours (cacao and coconut, then vanilla and acai) so will need the basic design adjusted for each flavour. The tubs are 1kg and this will need to be somewhere on the front of the tub.
This product is designed for healthy and active people, mainly female focused. The design should be clean and not overloaded with colours and pictures. It should only be two colours max. The final design should communicate that the product will assist people to reach their goals, whilst being health focused.

Target Market(s)

Active Females 20-50

Industry/Entity Type

Nutrition

Requirements
Must have
• Nutrition information and ingredients area
• Three logos attached
• Name- recovery formula
Should not have
• Not too busy, too many pictures or information. Please keep it simple.

```html
<!DOCTYPE html>
<html lang="en">
<head>
<meta charset="utf-8">
<title>LW Recovery Formula – Tub Labels</title>
<link rel="stylesheet" href="https://fonts.googleapis.com/css2?family=Bebas+Neue&family=Montserrat:wght@800&family=Oswald:wght@500&display=swap">
<style>
  :root {
    --page: #ffffff;
    --kraft-light: #b8976c;
    --kraft-mid: #a88257;
    --kraft-dark: #8b6834;
    --ink: #111111;
    --paper: #ffffff;
    --icon-tone: #6f5430;
  }
  * { box-sizing: border-box; margin: 0; padding: 0; }
  html, body { width: 1200px; height: 1040px; overflow: hidden; background: var(--page); }
  .canvas {
    width: 1200px; height: 1040px;
    display: flex; justify-content: center; align-items: center; gap: 90px;
  }
  .label {
    width: 480px; height: 760px;
    background: linear-gradient(90deg, var(--kraft-mid) 0%, var(--kraft-light) 35%, var(--kraft-mid) 70%, var(--kraft-dark) 100%);
    display: flex; flex-direction: column; align-items: center;
    padding-top: 230px;
  }
  .brand-mark {
    width: 134px; height: 134px; border-radius: 50%;
    background: var(--ink);
    display: flex; align-items: center; justify-content: center;
    flex-shrink: 0;
  }
  .brand-name {
    font-family: "Montserrat", sans-serif; font-weight: 800;
    font-size: 54px; color: var(--paper); letter-spacing: -1px;
  }
  .product-title {
    margin-top: 34px;
    width: 100%;
    text-align: center;
    white-space: nowrap;
    font-family: "Bebas Neue", sans-serif; font-weight: 400;
    font-size: 58px; line-height: 1; color: var(--paper);
    letter-spacing: 0;
  }
  .dots { display: flex; gap: 11px; margin-top: 28px; }
  .dots span { width: 13px; height: 13px; border-radius: 50%; background: var(--paper); }
  .flavour {
    margin-top: 18px;
    display: flex; align-items: center; gap: 10px;
  }
  .flavour-name {
    font-family: "Montserrat", sans-serif; font-weight: 800;
    font-size: 20px; color: var(--ink); white-space: nowrap;
  }
  .flavour-icon { width: 40px; height: 40px; border-radius: 50%; background: var(--icon-tone); flex-shrink: 0; }
  .flavour + .dots { margin-top: 18px; }
  .net-weight {
    margin-top: 44px;
    font-family: "Oswald", sans-serif; font-weight: 500;
    font-size: 14px; color: var(--ink); letter-spacing: 0.2px;
  }
</style>
</head>
<body>
<main class="canvas">
  <section class="label label--cacao-coconut">
    <div class="brand-mark"><span class="brand-name">LW</span></div>
    <h1 class="product-title">LW RECOVERY FORMULA</h1>
    <div class="dots"><span></span><span></span><span></span></div>
    <div class="flavour">
      <div class="flavour-icon" role="img" aria-label="Line icon of a cacao pod"></div>
      <span class="flavour-name">CACAO + COCONUT</span>
      <div class="flavour-icon" role="img" aria-label="Line icon of a coconut"></div>
    </div>
    <div class="dots"><span></span><span></span><span></span></div>
    <p class="net-weight">NET WT 1 KG</p>
  </section>

  <section class="label label--vanilla-acai">
    <div class="brand-mark"><span class="brand-name">LW</span></div>
    <h1 class="product-title">LW RECOVERY FORMULA</h1>
    <div class="dots"><span></span><span></span><span></span></div>
    <div class="flavour">
      <div class="flavour-icon" role="img" aria-label="Line icon of a vanilla flower and pods"></div>
      <span class="flavour-name">VANILLA + ACAI</span>
      <div class="flavour-icon" role="img" aria-label="Icon of an acai palm with berries"></div>
    </div>
    <div class="dots"><span></span><span></span><span></span></div>
    <p class="net-weight">NET WT 1 KG</p>
  </section>
</main>
</body>
</html>
```